Bref créative
Dale's Furniture
Stationary, Letterhead, Business Cards, Envelopes
I need single sided standard sized Business Card [3.5" x 2"]
Similar to Logo Font
Bright & Fun-filled
Dale's Furniture and Appliances
4817 W. Corvel Ave.
Chicago IL 60688
Dalesfurnitureandappliances@quillmail.example
www.dalesfurnitureandapplianes.example
Current Logo
Black and White Version

```html
<!DOCTYPE html>
<html lang="en">
<head>
<meta charset="utf-8">
<title>Dale's Furniture – Stationery Set</title>
<link href="https://fonts.googleapis.com/css2?family=Playfair+Display:wght@700&family=Roboto:wght@400;700&display=swap" rel="stylesheet">
<style>
  :root{
    --bg:#e8e5e0;
    --paper:#ffffff;
    --red:#e0161c;
    --red-dark:#a30b10;
    --black:#1b1b1b;
    --ink:#444444;
    --muted:#9a9a9a;
    --line:#d6d6d6;
    --watermark:#f3e4dc;
  }
  *{margin:0;padding:0;box-sizing:border-box}
  html,body{width:1200px;height:547px;overflow:hidden;background:var(--bg)}
  body{position:relative;font-family:'Roboto',Arial,sans-serif;color:var(--ink)}
  .piece{position:absolute;background:var(--paper);overflow:hidden;box-shadow:0 2px 6px rgba(0,0,0,.18)}
  .swoosh{position:absolute;left:0;width:100%}
  .brand{display:flex;align-items:center;gap:4px}
  .brand-mark{background:var(--red);flex:none}
  .brand-name{font-family:'Playfair Display',Georgia,serif;font-weight:700;color:var(--black);white-space:nowrap}
  .brand.on-red .brand-name{color:#fff}
  .brand.on-red .brand-mark{background:#fff}
  .contact{font-size:5px;line-height:1.55;color:var(--ink);white-space:nowrap}
  .contact .label{color:var(--red);font-weight:700}
  .sheet-tint{position:absolute;right:0;bottom:4px;width:100%;height:110px;background:linear-gradient(180deg,rgba(243,228,220,0),var(--watermark))}

  /* business card front */
  .card-front{left:24px;top:34px;width:125px;height:72px}
  .card-front .brand{position:absolute;left:8px;top:8px}
  .card-front .brand-mark{width:6px;height:6px}
  .card-front .brand-name{font-size:7px}
  .card-front .contact{position:absolute;left:8px;top:24px;font-size:3.6px}
  .card-front .swoosh{bottom:0;height:22px}

  /* business card back */
  .card-back{left:158px;top:34px;width:125px;height:72px;background:var(--red)}
  .card-back .brand{position:absolute;left:0;right:0;top:26px;justify-content:center}
  .card-back .brand-mark{width:7px;height:7px}
  .card-back .brand-name{font-size:10px}
  .card-back .swoosh{bottom:0;height:20px}

  /* envelope front */
  .env-front{left:24px;top:144px;width:384px;height:168px}
  .env-front .brand{position:absolute;left:14px;top:14px}
  .env-front .brand-mark{width:8px;height:8px}
  .env-front .brand-name{font-size:10px}
  .env-front .contact{position:absolute;left:14px;top:32px;font-size:4px}
  .env-front .swoosh{bottom:0;height:70px}

  /* envelope back */
  .env-back{left:24px;top:329px;width:384px;height:194px}
  .env-back .flap{position:absolute;left:0;top:0;width:100%;height:194px}
  .env-back .brand{position:absolute;left:0;right:0;top:30px;justify-content:center}
  .env-back .brand-mark{width:9px;height:9px}
  .env-back .brand-name{font-size:13px}

  /* letterhead + fax shared header */
  .sheet{top:12px;width:377px;height:528px}
  .letterhead{left:427px}
  .fax{left:813px}
  .sheet-head{position:absolute;left:22px;top:16px;display:flex;gap:18px;align-items:flex-start}
  .sheet-head .brand-mark{width:8px;height:8px}
  .sheet-head .brand-name{font-size:10px}
  .sheet-head .contact{font-size:4.6px;line-height:1.5}
  .sheet-base{position:absolute;left:0;bottom:0;width:100%;height:4px;background:linear-gradient(90deg,var(--red-dark),var(--red))}

  /* letter body */
  .letter{position:absolute;left:44px;top:88px;width:290px;font-size:4.6px;line-height:1.55;color:var(--ink)}
  .letter p{margin-bottom:6px}
  .letter .gap{margin-bottom:12px}
  .letter .sign{margin-top:22px}

  /* fax form */
  .fax-form{position:absolute;left:22px;top:52px;width:333px;height:410px;border:1px solid var(--line);background:var(--paper)}
  .fax-bar{height:16px;background:linear-gradient(90deg,#f2f2f2,#e6e6e6 60%,var(--red) 60%);position:relative}
  .fax-bar .title{position:absolute;right:12px;top:4px;font-size:7px;font-weight:700;color:#fff;letter-spacing:.5px;line-height:1}
  .fax-bar svg{position:absolute;right:38px;top:4px}
  .fax-row{display:flex;align-items:center;height:22px;padding:0 10px}
  .fax-row .label{width:26px;font-size:4.6px;text-align:center;color:var(--ink)}
  .fax-row .label.hot{background:var(--red);color:#fff;padding:3px 0;border-radius:1px}
  .fax-row .field{flex:1;margin-left:40px;height:9px;border:1px solid var(--line)}
  .fax-row.tall{height:40px;align-items:flex-start;padding-top:6px}
  .fax-row.tall .field{height:26px}
  .fax-notes{margin:8px 10px 0 76px;height:120px;border:1px solid var(--line)}
</style>
</head>
<body>

  <section class="piece card-front" aria-label="Business card front">
    <div class="brand"><span class="brand-mark"></span><span class="brand-name">Dale's Furniture</span></div>
    <div class="contact">
      4817 W. Corvel Ave.<br>Chicago IL 60688<br>
      <span class="label">T</span> (312) 555-0148<br>
      <span class="label">E</span> Dalesfurnitureandappliances@quillmail.example
    </div>
    <svg class="swoosh" viewBox="0 0 125 22" preserveAspectRatio="none">
      <path d="M0 14 C40 2 80 4 125 0 L125 22 L0 22Z" fill="var(--black)"/>
      <path d="M0 17 C40 6 80 8 125 4 L125 22 L0 22Z" fill="var(--red)"/>
    </svg>
  </section>

  <section class="piece card-back" aria-label="Business card back">
    <div class="brand on-red"><span class="brand-mark"></span><span class="brand-name">Dale's Furniture</span></div>
    <svg class="swoosh" viewBox="0 0 125 20" preserveAspectRatio="none">
      <path d="M0 20 C40 6 90 4 125 10 L125 20Z" fill="var(--black)"/>
    </svg>
  </section>

  <section class="piece env-front" aria-label="Envelope front">
    <div class="brand"><span class="brand-mark"></span><span class="brand-name">Dale's Furniture</span></div>
    <div class="contact">
      4817 W. Corvel Ave.<br>Chicago IL 60688<br>
      <span class="label">T</span> (312) 555-0148<br>
      <span class="label">E</span> Dalesfurnitureandappliances@quillmail.example
    </div>
    <svg class="swoosh" viewBox="0 0 384 70" preserveAspectRatio="none">
      <defs>
        <linearGradient id="envRed" x1="0" y1="0" x2="0" y2="1">
          <stop offset="0" stop-color="#ff3b3b"/><stop offset="1" stop-color="#b60c10"/>
        </linearGradient>
      </defs>
      <path d="M0 40 C120 8 260 6 384 30 L384 70 L0 70Z" fill="url(#envRed)"/>
      <path d="M0 58 C120 40 260 44 384 52 L384 70 L0 70Z" fill="var(--black)"/>
    </svg>
  </section>

  <section class="piece env-back" aria-label="Envelope back">
    <svg class="flap" viewBox="0 0 384 194" preserveAspectRatio="none">
      <defs>
        <linearGradient id="flapRed" x1="0" y1="0" x2="0" y2="1">
          <stop offset="0" stop-color="#ff3b3b"/><stop offset="1" stop-color="#b60c10"/>
        </linearGradient>
      </defs>
      <path d="M0 0 H384 V22 C300 46 240 70 192 74 C144 70 84 46 0 22Z" fill="url(#flapRed)"/>
      <path d="M0 22 C84 46 144 70 192 74 C240 70 300 46 384 22 V28 C300 52 240 76 192 80 C144 76 84 52 0 28Z" fill="var(--black)"/>
      <path d="M0 194 L150 110 L234 110 L384 194" fill="none" stroke="#d9d9d9" stroke-width="1"/>
      <path d="M0 30 L150 110 M384 30 L234 110" fill="none" stroke="#e4e4e4" stroke-width="1"/>
    </svg>
    <div class="brand on-red"><span class="brand-mark"></span><span class="brand-name">Dale's Furniture</span></div>
  </section>

  <section class="piece sheet letterhead" aria-label="Letterhead">
    <div class="sheet-tint"></div>
    <header class="sheet-head">
      <div class="brand"><span class="brand-mark"></span><span class="brand-name">Dale's Furniture</span></div>
      <div class="contact">
        4817 W. Corvel Ave.<br>Chicago IL 60688<br>
        <span class="label">T</span> (312) 555-0148<br>
        <span class="label">F</span> (312) 555-0149<br>
        <span class="label">E</span> Dalesfurnitureandappliances@quillmail.example
      </div>
    </header>
    <div class="letter">
      <p class="gap">June 12, 2024</p>
      <p class="gap">Jordan Avery<br>Avery Home Co.<br>22 Lakeview Rd.<br>Chicago IL 60601</p>
      <p>Dear Jordan,</p>
      <p>Thank you for visiting our showroom last week. We are glad you found pieces you love for your new home, and our team is ready to help with delivery and setup at a time that suits you.</p>
      <p>Your order includes the sofa, the oak dining set and two matching lamps. Each item is checked by hand before it leaves our store, so it arrives clean and ready to use.</p>
      <p>If you have questions about colours, sizes or care, please call us or stop by. We are open every day and always happy to talk furniture.</p>
      <p>We look forward to serving you again soon.</p>
      <p class="sign">Sincerely,<br><br>Dale Warren<br>Owner</p>
    </div>
    <div class="sheet-base"></div>
  </section>

  <section class="piece sheet fax" aria-label="Fax cover sheet">
    <div class="sheet-tint"></div>
    <header class="sheet-head">
      <div class="brand"><span class="brand-mark"></span><span class="brand-name">Dale's Furniture</span></div>
      <div class="contact">
        4817 W. Corvel Ave.<br>Chicago IL 60688<br>
        <span class="label">T</span> (312) 555-0148<br>
        <span class="label">F</span> (312) 555-0149<br>
        <span class="label">E</span> Dalesfurnitureandappliances@quillmail.example
      </div>
    </header>
    <div class="fax-form">
      <div class="fax-bar">
        <svg width="10" height="8" viewBox="0 0 10 8"><path d="M0 4 H7 M4 1 L7 4 L4 7" stroke="#fff" stroke-width="1.4" fill="none"/></svg>
        <span class="title">FAX</span>
      </div>
      <div class="fax-row"><span class="label hot">To</span><span class="field"></span></div>
      <div class="fax-row"><span class="label">Company</span><span class="field"></span></div>
      <div class="fax-row"><span class="label">Attention</span><span class="field"></span></div>
      <div class="fax-row"><span class="label">Fax</span><span class="field"></span></div>
      <div class="fax-row"><span class="label">Phone</span><span class="field"></span></div>
      <div class="fax-row tall"><span class="label hot">From</span><span class="field"></span></div>
      <div class="fax-row"><span class="label hot">Date</span><span class="field"></span></div>
      <div class="fax-row"><span class="label">Pages</span><span class="field"></span></div>
      <div class="fax-notes"></div>
    </div>
    <div class="sheet-base"></div>
  </section>

</body>
</html>
```